Every Drawer Neatly Sorted or EDN Organized needs a business card design. EDN Organized is a professi

We need a business card design that is clean, sharp and conveys a sense of organization. I already have a logo.

Target Market(s)

Families (specifically mothers), small business owners, parents, seniors

Industry/Entity Type

Business

Contact Information for Business Card

My website is www.ednorganized-example.com and my Facebook page is http://www.socialpage-example.com/everydrawerneatlysorted. The phone number is 555-418-2706 and I want to be listed as Miriel O. Dunsford, Owner

Requirements
Must have
• My logo.

```html
<!DOCTYPE html>
<html lang="en">
<head>
<meta charset="utf-8">
<title>EDN Organized — Business Card</title>
<link href="https://fonts.googleapis.com/css2?family=Arimo:wght@400&family=Questrial&display=swap" rel="stylesheet">
<style>
  :root {
    --backdrop: #2a2b2e;
    --card-black: #0d0d0e;
    --name-band: #161617;
    --silver-light: #f6f4f4;
    --silver-mid: #b7babe;
    --silver-dark: #8d9196;
    --band-white: #ffffff;
    --brand-blue: #2f6fb8;
    --tab-blue: #3fb0e6;
    --tab-fold: #2a86b8;
    --icon-blue: #1f5f9c;
    --accent-blue: #3aa3dc;
    --text-white: #ffffff;
  }
  html, body {
    margin: 0;
    width: 1200px;
    height: 1000px;
    overflow: hidden;
    background: var(--backdrop);
  }
  .business-card {
    position: absolute;
    left: 100px;
    top: 200px;
    width: 1000px;
    height: 600px;
    background: var(--card-black);
    overflow: hidden;
    box-shadow: 0 20px 50px rgba(0,0,0,.45);
  }
  .silver-panel {
    position: absolute;
    left: 0; top: 0;
    width: 480px; height: 600px;
    background: linear-gradient(180deg, var(--silver-light) 0%, var(--silver-mid) 38%, var(--silver-light) 50%, var(--silver-mid) 68%, var(--silver-dark) 100%);
  }
  .logo-band {
    position: absolute;
    left: 0; top: 290px;
    width: 480px; height: 120px;
    background: linear-gradient(90deg, #ececec 0%, var(--band-white) 30%, var(--band-white) 100%);
    display: flex;
    align-items: center;
    justify-content: center;
    gap: 16px;
  }
  .logo-mark {
    width: 22px; height: 22px;
    border-radius: 50%;
    background: var(--brand-blue);
  }
  .logo-name {
    font-family: "Questrial", sans-serif;
    font-size: 46px;
    color: var(--brand-blue);
    letter-spacing: 1px;
  }
  .name-band {
    position: absolute;
    left: 480px; top: 40px;
    width: 520px; height: 100px;
    background: var(--name-band);
    text-align: center;
  }
  .owner-name {
    margin: 16px 0 0;
    font-family: "Arimo", sans-serif;
    font-size: 30px;
    color: var(--text-white);
    letter-spacing: .5px;
  }
  .owner-title {
    margin: 8px 0 0;
    font-family: "Questrial", sans-serif;
    font-size: 28px;
    letter-spacing: 1px;
    color: var(--accent-blue);
  }
  .contact-row {
    position: absolute;
    left: 470px;
    display: flex;
    align-items: center;
  }
  .contact-row.web { top: 212px; }
  .contact-row.social { top: 312px; }
  .contact-row.phone { top: 412px; }
  .contact-tab { width: 130px; height: 70px; flex: none; }
  .contact-text {
    margin-left: 24px;
    font-family: "Arimo", sans-serif;
    color: var(--text-white);
    font-size: 32px;
  }
  .contact-row.social .contact-text { font-size: 27px; }
  .contact-row.phone .contact-text { font-size: 36px; }
</style>
</head>
<body>
  <main class="business-card">
    <div class="silver-panel"></div>
    <div class="logo-band">
      <span class="logo-mark"></span>
      <span class="logo-name">EDN Organized</span>
    </div>

    <header class="name-band">
      <p class="owner-name">MIRIEL O. DUNSFORD</p>
      <p class="owner-title">OWNER</p>
    </header>

    <div class="contact-row web">
      <svg class="contact-tab" viewBox="0 0 130 70" aria-hidden="true">
        <path d="M10 4 L10 66 L2 58 L2 12 Z" fill="var(--tab-fold)"/>
        <path d="M10 4 H96 A31 31 0 0 1 96 66 H10 Z" fill="var(--tab-blue)"/>
        <g fill="none" stroke="var(--icon-blue)" stroke-width="2.5">
          <circle cx="80" cy="35" r="17"/>
          <ellipse cx="80" cy="35" rx="7" ry="17"/>
          <line x1="63" y1="35" x2="97" y2="35"/>
          <path d="M66 26 H94 M66 44 H94"/>
        </g>
      </svg>
      <span class="contact-text">ednorganized-example.com</span>
    </div>

    <div class="contact-row social">
      <svg class="contact-tab" viewBox="0 0 130 70" aria-hidden="true">
        <path d="M10 4 L10 66 L2 58 L2 12 Z" fill="var(--tab-fold)"/>
        <path d="M10 4 H96 A31 31 0 0 1 96 66 H10 Z" fill="var(--tab-blue)"/>
        <rect x="64" y="19" width="32" height="32" rx="3" fill="var(--icon-blue)"/>
      </svg>
      <span class="contact-text">/everydrawerneatlysorted</span>
    </div>

    <div class="contact-row phone">
      <svg class="contact-tab" viewBox="0 0 130 70" aria-hidden="true">
        <path d="M10 4 L10 66 L2 58 L2 12 Z" fill="var(--tab-fold)"/>
        <path d="M10 4 H96 A31 31 0 0 1 96 66 H10 Z" fill="var(--tab-blue)"/>
        <circle cx="80" cy="35" r="18" fill="none" stroke="var(--icon-blue)" stroke-width="2.5"/>
        <path d="M72 25 l5 -1 3 7 -3 3 q3 6 8 8 l3 -3 7 3 -1 5 q-2 3 -6 2 q-12 -4 -17 -17 q-1 -4 1 -7 z" fill="var(--icon-blue)"/>
      </svg>
      <span class="contact-text">555-418-2706</span>
    </div>
  </main>
</body>
</html>
```